mechanical repair shop

our shop repairs light and medium duty trucks

we sell tires , do oil changes, engine and transmissions
vehicle accessories, alignments, brakes , exhaust, all major and minor repairs.

if you would like to get a hold of me email: gideon.marlowe@quillventa.example tel: 1-780-555-0148

Target Market(s)

light and medium duty trucks and cars

Industry/Entity Type

Shop

Colors
f37122

Requirements
Must have
• visual sales displays
Nice to have
• pictures

```html
<!DOCTYPE html>
<html lang="en">
<head>
<meta charset="utf-8">
<title>Quillventa Mechanical Repair Shop</title>
<link rel="stylesheet" href="https://fonts.googleapis.com/css2?family=Lato:wght@400;700&family=Open+Sans:wght@400;600;700&display=swap">
<style>
  :root{
    --orange:#f37122;
    --amber:#f2a21f;
    --amber-deep:#ee8c1c;
    --red:#e3161b;
    --charcoal:#1e1e1e;
    --charcoal-2:#2c2c2c;
    --silver:#d9d9d9;
    --white:#ffffff;
    --ink:#141414;
  }
  *{margin:0;padding:0;box-sizing:border-box;}
  html,body{width:877px;height:1200px;overflow:hidden;background:#e9e9e9;}
  .flyer{position:relative;width:877px;height:1200px;overflow:hidden;
    background:linear-gradient(180deg,var(--amber) 0%,var(--amber-deep) 100%);
    font-family:"Lato",sans-serif;}
  .layer{position:absolute;left:0;top:0;}
  .brand-badge{position:absolute;left:345px;top:-8px;width:186px;height:186px;border-radius:50%;
    background:radial-gradient(circle at 50% 40%,#2a2a2a,#050505 70%);
    border:8px solid var(--silver);box-shadow:0 0 0 3px #8a8a8a,0 6px 14px rgba(0,0,0,.5);
    display:flex;align-items:center;justify-content:center;}
  .brand-name{font-family:"Lato",sans-serif;font-weight:700;font-size:21px;letter-spacing:1px;color:var(--orange);margin-top:40px;}
  .headline{position:absolute;left:66px;top:712px;font-family:"Open Sans",sans-serif;line-height:1;}
  .headline .line-1{display:block;font-weight:700;font-size:48px;color:var(--red);letter-spacing:-.5px;}
  .headline .line-2{display:block;font-weight:400;font-size:51px;color:var(--white);margin-top:14px;}
  .services-tab{position:absolute;left:0;top:850px;width:182px;height:31px;border-radius:0 16px 16px 0;
    background:linear-gradient(180deg,#ffffff,#c9c9c9);padding-left:32px;
    font-family:"Open Sans",sans-serif;font-weight:700;font-size:20px;color:var(--red);line-height:31px;}
  .service{position:absolute;display:flex;align-items:center;gap:12px;font-size:16px;color:var(--ink);}
  .service-icon{width:46px;height:46px;border-radius:50%;background:var(--charcoal);
    border:2px solid #bdbdbd;display:flex;align-items:center;justify-content:center;flex:none;}
  .contact-bar{position:absolute;left:0;top:1122px;width:877px;height:78px;}
  .contact{position:absolute;top:1143px;display:flex;align-items:center;gap:8px;font-size:18px;color:var(--white);}
</style>
</head>
<body>
<main class="flyer">

  <!-- structure: dark header, photo areas, curves -->
  <svg class="layer" width="877" height="1200" viewBox="0 0 877 1200" aria-hidden="true">
    <defs>
      <linearGradient id="header-fill" x1="0" y1="0" x2="0" y2="1">
        <stop offset="0" stop-color="#262626"/><stop offset="1" stop-color="#121212"/>
      </linearGradient>
      <linearGradient id="bar-fill" x1="0" y1="0" x2="0" y2="1">
        <stop offset="0" stop-color="#2e2e2e"/><stop offset="1" stop-color="#151515"/>
      </linearGradient>
    </defs>
    <path d="M0,0 H877 V285 Q438,130 0,285 Z" fill="url(#header-fill)"/>
    <rect x="0" y="40" width="877" height="10" fill="var(--silver)"/>
    <path d="M0,290 Q438,150 877,290 L877,310 Q438,185 0,310 Z" fill="var(--orange)"/>
  </svg>

  <svg class="layer" width="877" height="1200" viewBox="0 0 877 1200" role="img" aria-label="Photo of a bright repair workshop with cars raised on blue lifts">
    <defs>
      <linearGradient id="garage-fill" x1="0" y1="0" x2="1" y2="1">
        <stop offset="0" stop-color="#e8ecef"/><stop offset=".45" stop-color="#c9d2da"/>
        <stop offset=".75" stop-color="#9aa3ab"/><stop offset="1" stop-color="#d6d9dc"/>
      </linearGradient>
    </defs>
    <path d="M0,305 Q438,175 877,305 L877,780 C600,760 360,670 210,540 C130,470 60,425 0,395 Z" fill="url(#garage-fill)"/>
    <path d="M0,395 C60,425 130,470 210,540 C360,670 600,760 877,780" fill="none" stroke="var(--white)" stroke-width="14"/>
    <path d="M0,407 C60,437 130,482 205,552 C355,684 600,774 877,794" fill="none" stroke="var(--red)" stroke-width="10"/>
  </svg>

  <svg class="layer" width="877" height="1200" viewBox="0 0 877 1200" role="img" aria-label="Photo of a white sports car in motion">
    <defs>
      <linearGradient id="motion-fill" x1="0" y1="0" x2="1" y2="1">
        <stop offset="0" stop-color="#8a8f94"/><stop offset=".5" stop-color="#eef0f2"/><stop offset="1" stop-color="#4b4f53"/>
      </linearGradient>
    </defs>
    <circle cx="197" cy="588" r="110" fill="var(--silver)"/>
    <circle cx="197" cy="588" r="103" fill="var(--red)"/>
    <circle cx="197" cy="588" r="96" fill="url(#motion-fill)"/>
  </svg>

  <svg class="layer" width="877" height="1200" viewBox="0 0 877 1200" role="img" aria-label="Photo of a white convertible in a showroom">
    <defs>
      <linearGradient id="showroom-fill" x1="0" y1="0" x2="0" y2="1">
        <stop offset="0" stop-color="#e4e4e2"/><stop offset=".55" stop-color="#f7f7f7"/><stop offset="1" stop-color="#9c9c9c"/>
      </linearGradient>
    </defs>
    <path d="M877,778 L712,784 Q596,955 672,1126 L877,1126 Z" fill="var(--white)"/>
    <path d="M877,786 L718,791 Q606,955 682,1126 L877,1126 Z" fill="var(--red)"/>
    <path d="M877,793 L724,797 Q616,955 692,1126 L877,1126 Z" fill="url(#showroom-fill)"/>
  </svg>

  <div class="brand-badge"><span class="brand-name">QUILLVENTA</span></div>

  <h1 class="headline"><span class="line-1">MECHANICAL</span><span class="line-2">REPAIR SHOP</span></h1>

  <div class="services-tab">SERVICES</div>

  <div class="service" style="left:40px;top:905px;">
    <span class="service-icon"><svg width="26" height="26" viewBox="0 0 26 26"><circle cx="13" cy="13" r="11" fill="none" stroke="#fff" stroke-width="3"/><circle cx="13" cy="13" r="4" fill="#fff"/></svg></span>Sell tires</div>
  <div class="service" style="left:193px;top:905px;">
    <span class="service-icon"><svg width="28" height="22" viewBox="0 0 28 22"><path d="M3,8 H17 L25,4 V7 L19,16 H3 Z" fill="#fff"/><rect x="8" y="4" width="5" height="4" fill="#fff"/><path d="M25,12 q2,3 0,5 q-2,-2 0,-5z" fill="#fff"/></svg></span>Oil changes</div>
  <div class="service" style="left:350px;top:905px;">
    <span class="service-icon"><svg width="28" height="22" viewBox="0 0 28 22"><path d="M5,6 H19 L23,10 H26 V17 H23 L20,20 H8 L5,16 H2 V9 H5 Z" fill="#fff"/><rect x="9" y="2" width="8" height="3" fill="#fff"/></svg></span>Engine and transmissions</div>

  <div class="service" style="left:40px;top:967px;">
    <span class="service-icon"><svg width="28" height="22" viewBox="0 0 28 22"><path d="M4,10 L7,3 H21 L24,10 H26 V18 H2 V10 Z" fill="#fff"/><rect x="9" y="5" width="10" height="4" fill="#1e1e1e"/><circle cx="7" cy="14" r="2" fill="#1e1e1e"/><circle cx="21" cy="14" r="2" fill="#1e1e1e"/></svg></span>Vehicle accessories</div>
  <div class="service" style="left:268px;top:967px;">
    <span class="service-icon"><svg width="24" height="22" viewBox="0 0 24 22"><rect x="2" y="2" width="20" height="3" fill="#fff"/><rect x="6" y="8" width="16" height="3" fill="#fff"/><rect x="2" y="14" width="20" height="3" fill="#fff"/><rect x="8" y="19" width="14" height="2" fill="#fff"/></svg></span>Alignments</div>
  <div class="service" style="left:420px;top:967px;">
    <span class="service-icon"><svg width="26" height="26" viewBox="0 0 26 26"><circle cx="13" cy="13" r="11" fill="none" stroke="#fff" stroke-width="2.5"/><circle cx="13" cy="13" r="6" fill="none" stroke="#fff" stroke-width="2"/><circle cx="13" cy="13" r="2" fill="#fff"/></svg></span>Brakes</div>

  <div class="service" style="left:40px;top:1029px;">
    <span class="service-icon"><svg width="26" height="26" viewBox="0 0 26 26"><path d="M4,4 L22,22" stroke="#fff" stroke-width="3.5" stroke-linecap="round"/><path d="M22,4 L4,22" stroke="#fff" stroke-width="3" stroke-linecap="round"/><circle cx="21" cy="5" r="3.5" fill="none" stroke="#fff" stroke-width="2"/></svg></span>Exhaust all major and Minor repairs</div>

  <svg class="contact-bar" width="877" height="78" viewBox="0 0 877 78" aria-hidden="true">
    <path d="M0,30 Q0,4 30,4 H847 Q877,4 877,30 V78 H0 Z" fill="var(--silver)"/>
    <path d="M0,34 Q0,10 30,10 H847 Q877,10 877,34 V78 H0 Z" fill="url(#bar-fill)"/>
  </svg>

  <div class="contact" style="left:40px;">
    <svg width="18" height="18" viewBox="0 0 24 24"><path d="M6.6 10.8a15 15 0 0 0 6.6 6.6l2.2-2.2a1 1 0 0 1 1-.25 11.4 11.4 0 0 0 3.6.57 1 1 0 0 1 1 1V20a1 1 0 0 1-1 1A17 17 0 0 1 3 4a1 1 0 0 1 1-1h3.5a1 1 0 0 1 1 1c0 1.25.2 2.45.57 3.57a1 1 0 0 1-.25 1z" fill="var(--orange)"/></svg>1-780-555-0148</div>
  <div class="contact" style="left:245px;">
    <svg width="20" height="14" viewBox="0 0 20 14"><rect x="0" y="0" width="20" height="14" fill="var(--orange)"/><path d="M0,0 L10,8 L20,0" fill="none" stroke="#1e1e1e" stroke-width="1.6"/></svg>gideon.marlowe@quillventa.example</div>
  <div class="contact" style="left:640px;">
    <svg width="18" height="18" viewBox="0 0 18 18"><circle cx="9" cy="9" r="8" fill="none" stroke="var(--orange)" stroke-width="1.8"/><ellipse cx="9" cy="9" rx="3.5" ry="8" fill="none" stroke="var(--orange)" stroke-width="1.5"/><path d="M1,9 H17 M2.5,5 H15.5 M2.5,13 H15.5" stroke="var(--orange)" stroke-width="1.3"/></svg>quillventa.example</div>

</main>
</body>
</html>
```